Zelmor Harbor Advisors Website

We are interested in developing a complete website and long term maintenance with the developer we choose through this contest.

Zelmor is a financial consulting company. We will have a website that capitalizes on the initial costs of retaining a client by providing additional services the client needs and tyically spend using 3rd parties.

The primary function of the website will be structured as a sales tool to retain and provide financial services to the client. Also, to provide other services that are integral to starting, building, and growing a business in order to increase creditibility and maintain client loyalty.

Through a combination of in-house "white label" services as well well chosen outside professional services as "affiliates".

The website home page must be a an instant curb-side appeal and representation of our desired extraordinary image. That image is a robust, innovative (zElmor), with a sophistication that creates an instant emotion of excitement and confidence that they have finally found that "needle in the haystack" they have been seeking. The feeling that they are compelled to take action lest they lose our contact information and are doomed to sink to the mediocrity that most business accept through a lack of effort and forsite.
Updates

Reason: Emails were going to the wrong account and I didn't receive any notices of questions or designs being posted.

Target Market(s)

Startup, growth and advancing companies seeking capital and other business services such as website and corporate image design, legal, marketing, asset management, investment and business consulting, etc.

Industry/Entity Type

Financial

Requirements
Must have
• We want to see your creativity
Nice to have
Should not have

```html
<!DOCTYPE html>
<html lang="en">
<head>
<meta charset="utf-8">
<title>zElmor – Home</title>
<link href="https://fonts.googleapis.com/css2?family=Arimo:wght@400;700&family=Open+Sans:wght@400&display=swap" rel="stylesheet">
<style>
:root{
  --orange:#e0560c;
  --orange-light:#f47a2a;
  --blue:#1565c0;
  --blue-light:#3f8ede;
  --link:#1a5fb4;
  --text:#222;
  --muted:#333;
  --brand:#2b3a4a;
  --rule:#b9c3cc;
  --card-border:#dcdcdc;
  --page:#ffffff;
  --band:#eef0f2;
  --footer-top:#f4f4f4;
  --footer-bottom:#dedede;
}
*{box-sizing:border-box;margin:0;padding:0}
html,body{width:1200px;height:902px;overflow:hidden}
body{position:relative;font-family:"Arimo",Arial,sans-serif;color:var(--text);
  background:linear-gradient(to bottom,#dfe1e4 0,var(--band) 60px,var(--band) 232px,var(--page) 244px,var(--page) 100%)}
.site-header{position:absolute;left:0;top:0;width:1200px;height:59px;
  background:linear-gradient(#ffffff,#eceded);box-shadow:0 1px 3px rgba(0,0,0,.25)}
.brand{position:absolute;left:30px;top:6px}
.brand-name{font-size:42px;font-weight:400;color:var(--brand);line-height:48px}
.main-nav{position:absolute;left:261px;top:0;display:flex;gap:1px}
.main-nav a{display:block;width:182px;height:57px;line-height:55px;text-align:center;
  font-size:15px;color:#fff;text-decoration:none;border-radius:0 0 8px 8px;
  background:linear-gradient(var(--blue-light),var(--blue) 45%,#0d57ad)}
.main-nav a.is-active{background:linear-gradient(var(--orange-light),var(--orange) 45%,#d14c06)}
.hero{position:absolute;left:28px;top:84px;width:1145px;height:306px;border-radius:9px;
  background:radial-gradient(ellipse at 30% 80%,#1f6b4a 0,transparent 45%),
             linear-gradient(100deg,#143a52 0,#2a2f78 55%,#2b2468 100%);
  box-shadow:0 2px 6px rgba(0,0,0,.35)}
.card{position:absolute;top:424px;width:363px;height:412px;background:#fff;
  border:1px solid var(--card-border);border-radius:10px;box-shadow:0 1px 4px rgba(0,0,0,.18)}
.card-welcome{left:33px}.card-services{left:420px}.card-testimonials{left:805px}
.card-head{position:absolute;left:6px;top:7px;width:351px;height:61px;border-radius:8px 8px 0 0;
  color:#fff;font-family:"Open Sans",Arial,sans-serif;font-size:30px;font-weight:400;line-height:61px;padding-left:22px}
.card-welcome .card-head{background:linear-gradient(var(--orange-light),var(--orange) 50%,#d84f08)}
.card-services .card-head,.card-testimonials .card-head{background:linear-gradient(var(--blue-light),var(--blue) 50%,#0f5cb5)}
.card-icon{position:absolute;right:10px;top:4px}
.welcome-text{position:absolute;left:15px;top:86px;width:326px;font-size:13.5px;line-height:21px;
  text-align:justify;color:var(--muted);hyphens:auto}
.service-list{position:absolute;left:25px;top:87px;width:312px;list-style:none}
.service-list li{height:35px;line-height:32px;border-bottom:1px dotted var(--rule);
  font-size:14px;color:var(--link);padding-left:15px;position:relative}
.service-list li:last-child{border-bottom:0}
.service-list li::before{content:"";position:absolute;left:0;top:13px;border:4px solid transparent;
  border-left:6px solid #2196e0;border-right:0}
.testimonial-list{position:absolute;left:28px;top:92px;list-style:none}
.testimonial-list li{height:51px;padding-left:24px;position:relative;font-size:14px;line-height:17px}
.testimonial-list li svg{position:absolute;left:0;top:2px}
.testimonial-list .quote-title{color:var(--link)}
.testimonial-list .quote-date{color:var(--muted)}
.btn-more{position:absolute;right:14px;bottom:19px;width:97px;height:35px;border-radius:7px;
  background:linear-gradient(var(--orange-light),var(--orange) 55%,#cf4a05);color:#fff;
  font-size:12.5px;line-height:35px;text-align:center;text-decoration:none;box-shadow:0 1px 2px rgba(0,0,0,.3)}
.site-footer{position:absolute;left:0;top:857px;width:1200px;height:45px;
  background:linear-gradient(var(--footer-top),var(--footer-bottom));border-top:1px solid #cfcfcf;
  font-size:13px;color:#222}
.footer-nav{position:absolute;left:27px;top:15px}
.footer-nav a{color:#222;text-decoration:none}
.footer-nav .sep{margin:0 9px}
.copyright{position:absolute;right:27px;top:15px}
</style>
</head>
<body>
<header class="site-header">
  <div class="brand"><span class="brand-name">zElmor</span></div>
  <nav class="main-nav">
    <a class="is-active" href="#">Home</a><a href="#">About Us</a><a href="#">Services</a><a href="#">Solutions</a><a href="#">Contact Us</a>
  </nav>
</header>

<div class="hero" role="img" aria-label="Stock market candlestick chart glowing in blue and green with a pen pointing at it"></div>

<section class="card card-welcome">
  <h2 class="card-head">Welcome!
    <svg class="card-icon" width="54" height="54" viewBox="0 0 54 54"><ellipse cx="27" cy="23" rx="22" ry="18" fill="#bfe3fb" stroke="#6fb6e6" stroke-width="2"/><path d="M16 37 L12 50 L26 40Z" fill="#bfe3fb" stroke="#6fb6e6" stroke-width="2"/></svg>
  </h2>
  <p class="welcome-text">Lorem Ipsum is simply dummy text of the printing and typesetting industry. Lorem Ipsum has been the industry's standard dummy text ever since the 1500s, when an unknown printer took a galley of type and scrambled it to make a type specimen book. It has survived not only five centuries, but also the leap into electronic typesetting, remaining essentially unchanged. It was popularised in the 1960s with the release of Pressline sheets containing Lorem Ipsum passages, and more recently with desktop publishing software like Quillset Layout including versions of Lorem Ipsum.</p>
  <a class="btn-more" href="#">Read More</a>
</section>

<section class="card card-services">
  <h2 class="card-head">Services
    <svg class="card-icon" width="54" height="54" viewBox="0 0 54 54"><g fill="#c9c9c9" stroke="#888" stroke-width="1.5"><circle cx="27" cy="27" r="18"/><g stroke-width="0"><rect x="23" y="3" width="8" height="10" rx="2"/><rect x="23" y="41" width="8" height="10" rx="2"/><rect x="3" y="23" width="10" height="8" rx="2"/><rect x="41" y="23" width="10" height="8" rx="2"/></g></g><circle cx="27" cy="27" r="8" fill="#5b7fa8" stroke="#666"/></svg>
  </h2>
  <ul class="service-list">
    <li>Webdesign</li><li>Capital Raising</li><li>Legal, Accounting</li><li>Financing, Sales Forces</li><li>Printing</li>
  </ul>
  <a class="btn-more" href="#">Read More</a>
</section>

<section class="card card-testimonials">
  <h2 class="card-head">Testimonials
    <svg class="card-icon" width="54" height="54" viewBox="0 0 54 54"><rect x="5" y="3" width="40" height="48" fill="#fdfbf2" stroke="#999"/><g stroke="#bbb"><line x1="10" y1="16" x2="40" y2="16"/><line x1="10" y1="23" x2="40" y2="23"/><line x1="10" y1="30" x2="40" y2="30"/><line x1="10" y1="37" x2="34" y2="37"/></g><path d="M48 14 L30 42 L27 47 L32 44 L50 17Z" fill="#f2a31c" stroke="#8a5a10"/></svg>
  </h2>
  <ul class="testimonial-list">
    <li><svg width="18" height="18" viewBox="0 0 16 16"><path d="M2 3h11v7H7l-4 4v-4H2z" fill="#f5d67a" stroke="#b58a2a"/></svg><div class="quote-title">Sorem porttitor.</div><div class="quote-date">2 years 40 weeks ago</div></li>
    <li><svg width="18" height="18" viewBox="0 0 16 16"><path d="M2 3h11v7H7l-4 4v-4H2z" fill="#f5d67a" stroke="#b58a2a"/></svg><div class="quote-title">Sorem porttitor.</div><div class="quote-date">2 years 40 weeks ago</div></li>
    <li><svg width="18" height="18" viewBox="0 0 16 16"><path d="M2 3h11v7H7l-4 4v-4H2z" fill="#f5d67a" stroke="#b58a2a"/></svg><div class="quote-title">Sorem porttitor.</div><div class="quote-date">2 years 40 weeks ago</div></li>
    <li><svg width="18" height="18" viewBox="0 0 16 16"><path d="M2 3h11v7H7l-4 4v-4H2z" fill="#f5d67a" stroke="#b58a2a"/></svg><div class="quote-title">Sorem porttitor.</div><div class="quote-date">2 years 40 weeks ago</div></li>
    <li><svg width="18" height="18" viewBox="0 0 16 16"><path d="M2 3h11v7H7l-4 4v-4H2z" fill="#f5d67a" stroke="#b58a2a"/></svg><div class="quote-title">Sorem porttitor.</div><div class="quote-date">2 years 40 weeks ago</div></li>
  </ul>
  <a class="btn-more" href="#">Read More</a>
</section>

<footer class="site-footer">
  <nav class="footer-nav"><a href="#">Home</a><span class="sep">I</span><a href="#">About Us</a><span class="sep">I</span><a href="#">Services</a><span class="sep">I</span><a href="#">Solutions</a><span class="sep">I</span><a href="#">Contact Us</a></nav>
  <div class="copyright">zElmor © 2011. All Rights Reserved</div>
</footer>
</body>
</html>
```